Circular Wedding Menu Design - Adobe Illustrator

I am looking for a design for circular wedding menus. these will be 7 inches.I'm providing a template from the printer, AI files of our wedding invitation, and the menu items.

The paper our invitations were printed on was a sandy beige color. please make the background for this the same color. It will be put ontop of a white plate with ivory tablecloth and cappucino covered napkins.

IMPORTANT - We aren't committed to a specific design so feel free to use whatever you like, but we definitely want the cow, fish, and carrot images from our rsvp to be used for the entrees in the menu.

IMPORTANT - must be in Adobe illustrator format

for inspiration:
http://cdn.plumbridalpages.example/wp-content/uploads/2012/10/harvel-styled-19.jpg

http://www.pictofind.example/imgres?imgurl=http%3A%2F%2Fwww.velvetknotstudio.example%2Fblog%2Fwp-content%2Fuploads%2F2013%2F07%2FRound-Menu-Wedding-Place-Setting.jpg&imgrefurl=http%3A%2F%2Fwww.velvetknotstudio.example%2Fblog%2Finspiration%2Fsimply-lovely-wedding-menu-place-settings%2F&h=815&w=600&zoom=1&page=1&start=0&ndsp=30

https://thumbs3.pictofind.example/images?q=tbn:Xk4mPq7RtL2vNw9HbYc3JdZs8FgQe1Ua

https://thumbs3.pictofind.example/images?q=tbn:Rb6wLn2TqZ8kVe4MhXs1PcYj9DuGa3Wo

https://thumbs2.pictofind.example/images?q=tbn:Hn5cWq8JtM3sLz7PxVb2KeRd6YgFo1Ni

```html
<!DOCTYPE html>
<html lang="en">
<head>
<meta charset="utf-8">
<title>Wedding Menu</title>
<link rel="stylesheet" href="https://fonts.googleapis.com/css2?family=Pinyon+Script&family=Merienda:wght@400;600&display=swap">
<style>
  :root {
    --page: #ffffff;
    --sand: #fde8d8;
    --leaf-gold: #f0c27a;
    --leaf-soft: #f7d9b0;
    --ink: #111111;
  }
  html, body {
    margin: 0;
    padding: 0;
    width: 1200px;
    height: 1200px;
    overflow: hidden;
    background: var(--page);
  }
  .menu-card {
    position: relative;
    width: 1200px;
    height: 1200px;
    border-radius: 50%;
    overflow: hidden;
    background: var(--sand);
    color: var(--ink);
  }
  .foliage {
    position: absolute;
    inset: 0;
  }
  .menu-title {
    position: absolute;
    top: 40px;
    left: 0;
    width: 100%;
    margin: 0;
    text-align: center;
    font-family: "Pinyon Script", cursive;
    font-weight: 400;
    font-size: 290px;
    line-height: 1;
  }
  .course-heading {
    position: absolute;
    left: 0;
    width: 100%;
    margin: 0;
    text-align: center;
    font-family: "Merienda", cursive;
    font-weight: 600;
    font-style: italic;
    font-size: 40px;
    line-height: 1;
  }
  .dish {
    position: absolute;
    left: 0;
    width: 100%;
    margin: 0;
    text-align: center;
    font-family: "Merienda", cursive;
    font-style: italic;
    font-size: 18px;
    line-height: 34px;
  }
  .dish span { display: block; }
  .entree-icon {
    position: absolute;
    left: 50%;
    transform: translateX(-50%);
    background: var(--ink);
  }
  .icon-beef { top: 560px; width: 72px; height: 52px; border-radius: 12px; }
  .icon-fish { top: 704px; width: 66px; height: 46px; border-radius: 50%; }
  .icon-veg  { top: 836px; width: 34px; height: 58px; border-radius: 40% 40% 50% 50% / 20% 20% 80% 80%; }
</style>
</head>
<body>
<main class="menu-card">
  <svg class="foliage" width="1200" height="1200" viewBox="0 0 1200 1200" role="img" aria-label="Golden line-drawn leafy vines climbing from the lower edge and up the right side">
    <defs>
      <radialGradient id="leaf-wash-right" cx="0.9" cy="0.55" r="0.6">
        <stop offset="0" stop-color="var(--leaf-soft)" stop-opacity="0.9"/>
        <stop offset="1" stop-color="var(--leaf-soft)" stop-opacity="0"/>
      </radialGradient>
      <radialGradient id="leaf-wash-bottom" cx="0.5" cy="1" r="0.7">
        <stop offset="0" stop-color="var(--leaf-soft)" stop-opacity="0.9"/>
        <stop offset="1" stop-color="var(--leaf-soft)" stop-opacity="0"/>
      </radialGradient>
    </defs>
    <rect x="600" y="280" width="600" height="920" fill="url(#leaf-wash-right)"/>
    <rect x="0" y="640" width="1200" height="560" fill="url(#leaf-wash-bottom)"/>
  </svg>

  <h1 class="menu-title">Menu</h1>

  <h2 class="course-heading" style="top:342px">Salad</h2>
  <p class="dish" style="top:392px">
    <span>Grilled Watermelon &amp; Fig Salad</span>
    <span>Gem Lettuces, Watermelon, Figs, Toasted Hazelnuts,</span>
    <span>Balsamic Reduction, Honey-Orange Dressing</span>
  </p>

  <h2 class="course-heading" style="top:504px">Entrée</h2>

  <div class="entree-icon icon-beef" role="img" aria-label="Cow icon for the beef entrée"></div>
  <p class="dish" style="top:618px">
    <span>Beef Roasted Filet Mignon, Wild Mushrooms,</span>
    <span>Garlic Mashed Potatoes, Asparagus with Red Wine Sauce</span>
  </p>

  <div class="entree-icon icon-fish" role="img" aria-label="Fish icon for the fish entrée"></div>
  <p class="dish" style="top:757px">
    <span>Porcini Crusted Halibut, Lemon-Herb Potatoes,</span>
    <span>Black Kale, Early Girl Tomatoes</span>
  </p>

  <div class="entree-icon icon-veg" role="img" aria-label="Carrot icon for the vegetarian entrée"></div>
  <p class="dish" style="top:895px">
    <span>Artichoke Agnolotti, Wild Mushrooms,</span>
    <span>Baby Arugula, Goat Cheese, White Wine Sauce, Micro herbs</span>
  </p>

  <h2 class="course-heading" style="top:974px">Wedding Cake</h2>
  <p class="dish" style="top:1017px">
    <span>Delicate Butter Pecan With Fresh Raspberry Mouse</span>
  </p>
</main>
</body>
</html>
```